Tarrow Consulting WA Business Card

Create an interesting, eye catching and colourful two sided business card. We are a business consulting operation assisting SME's improve all areas of their business. We provide consulting services to assist SME's to create a culture of continuous improvement, making a positive difference in the business. Our tag line is Small changes, big rewards. We want to create a well recognised, innovative brand that can be continued throughout our website, social media and email correspondence.

Target Market(s)

Small to Medium Enterprise Business Owners

Industry/Entity Type

Business Consultant

Contact Information for Business Card

Name of Business: Tarrow Consulting - Steady Steps Strong Results
Dean Fordyce Ph 0407358114 Moira Fordyce Ph 0407935281
Email tarrowconsultingwa@mailbox-example.com
Web address TBA
FaceBook page TBA

BACKSIDE OF CARD

Providing assistance with:

• Organisation & Efficiency
• Revenue generation & Marketing
• Financial Management
• Production quality & delivery
• Systems & Process documentation
• Exit Strategy

Font styles to use
Other font styles liked:
• Calibri

Colors

Designer to choose colors to be used in the design.

Requirements
Must have
• Calibri font

```html
<!DOCTYPE html>
<html lang="en">
<head>
<meta charset="utf-8">
<title>Tarrow Consulting WA – Business Card</title>
<link href="https://fonts.googleapis.com/css2?family=Carlito:wght@400;700&display=swap" rel="stylesheet">
<style>
  :root {
    --backdrop: #1f1f20;
    --card: #1b1b1c;
    --card-edge: #262627;
    --brand-blue: #4a86c8;
    --brand-red: #d9412f;
    --text-light: #f2f2f2;
  }
  * { box-sizing: border-box; margin: 0; padding: 0; }
  html, body {
    width: 1200px; height: 900px; overflow: hidden;
    background: var(--backdrop);
    font-family: "Carlito", "Calibri", sans-serif;
  }
  .canvas {
    width: 1200px; height: 900px;
    display: flex; flex-direction: column; align-items: center; justify-content: center;
    gap: 34px;
  }
  .card {
    position: relative;
    width: 700px; height: 400px;
    background: radial-gradient(ellipse at 75% 70%, var(--card-edge), var(--card) 70%);
    border-bottom: 6px solid var(--brand-blue);
    box-shadow: 0 10px 30px rgba(0,0,0,0.55);
  }
  .brand { display: flex; align-items: center; gap: 16px; white-space: nowrap; }
  .brand-square { width: 34px; height: 34px; background: var(--brand-blue); flex: none; }
  .brand-name { font-weight: 700; color: var(--brand-blue); line-height: 1; letter-spacing: 0.5px; }
  .brand-tagline { color: var(--brand-red); letter-spacing: 1px; margin-top: 4px; }

  /* front */
  .card-front .brand { position: absolute; left: 50%; top: 50%; transform: translate(-50%, -56%); }
  .card-front .brand-name { font-size: 44px; }
  .card-front .brand-tagline { font-size: 21px; }

  /* back */
  .card-back .brand { position: absolute; left: 26px; top: 160px; gap: 10px; }
  .card-back .brand-square { width: 26px; height: 26px; }
  .card-back .brand-name { font-size: 29px; }
  .card-back .brand-tagline { font-size: 15px; }
  .divider {
    position: absolute; left: 332px; top: 42px; width: 3px; height: 300px;
    background: var(--brand-blue);
  }
  .details { position: absolute; left: 354px; top: 40px; right: 12px; white-space: nowrap; }
  .people {
    color: var(--brand-blue); font-weight: 700; font-size: 28px;
    letter-spacing: 1px; line-height: 1.1; text-transform: uppercase;
    margin-bottom: 12px;
  }
  .contacts { list-style: none; color: var(--text-light); font-size: 15px; line-height: 1.35; margin-bottom: 12px; }
  .contacts li { display: flex; align-items: center; gap: 8px; }
  .contacts svg { width: 11px; height: 11px; flex: none; }
  .web-domain { color: var(--brand-red); font-weight: 700; }
  .services { list-style: none; color: var(--text-light); font-size: 19px; line-height: 1.2; }
  .services li::before { content: ">"; color: var(--brand-blue); margin-right: 6px; }
</style>
</head>
<body>
<main class="canvas">
  <section class="card card-front" aria-label="Card front">
    <div class="brand">
      <span class="brand-square"></span>
      <div>
        <div class="brand-name">Tarrow Consulting</div>
        <div class="brand-tagline">Steady Steps Strong Results</div>
      </div>
    </div>
  </section>

  <section class="card card-back" aria-label="Card back">
    <div class="brand">
      <span class="brand-square"></span>
      <div>
        <div class="brand-name">Tarrow Consulting</div>
        <div class="brand-tagline">Steady Steps Strong Results</div>
      </div>
    </div>
    <div class="divider"></div>
    <div class="details">
      <div class="people">Dean Fordyce<br>Moira Fordyce</div>
      <ul class="contacts">
        <li><svg viewBox="0 0 12 12"><path d="M3 1 L5 3.5 L4 5 Q5 7 7 8 L8.5 7 L11 9 L9.5 11 Q4 10.5 1 3 Z" fill="var(--brand-blue)"/></svg>0407358114</li>
        <li><svg viewBox="0 0 12 12"><path d="M3 1 L5 3.5 L4 5 Q5 7 7 8 L8.5 7 L11 9 L9.5 11 Q4 10.5 1 3 Z" fill="var(--brand-blue)"/></svg>0407935281</li>
        <li><svg viewBox="0 0 12 12"><rect x="1" y="2.5" width="10" height="7" fill="none" stroke="var(--brand-blue)" stroke-width="1.2"/><path d="M1 2.5 L6 6.5 L11 2.5" fill="none" stroke="var(--brand-blue)" stroke-width="1.2"/></svg>tarrowconsultingwa@mailbox-example.com</li>
        <li><svg viewBox="0 0 12 12"><circle cx="6" cy="6" r="5" fill="none" stroke="var(--brand-blue)" stroke-width="1.2"/><ellipse cx="6" cy="6" rx="2.2" ry="5" fill="none" stroke="var(--brand-blue)" stroke-width="1"/><path d="M1 6 H11" stroke="var(--brand-blue)" stroke-width="1"/></svg><span>www.<span class="web-domain">tarrowconsultingwa</span>.com</span></li>
      </ul>
      <ul class="services">
        <li>Organisation &amp; Efficiency</li>
        <li>Revenue generation &amp; Marketing</li>
        <li>Financial Management</li>
        <li>Production quality &amp; delivery</li>
        <li>Systems &amp; Process documentation</li>
        <li>Exit Strategy</li>
      </ul>
    </div>
  </section>
</main>
</body>
</html>
```